Tildens Biscuit Barn Website

I need a website for a diner/restaurant that has been established in a farming, oil and industrial community for over 15 years. The website needs to be simple in design, but that should demonstrate the mastery of skills of the designer. Our diner/restaurant is family oriented, patriotic but very rustic
Fb Address is fb.me/TildensBarn

Pictures of the restaurant

https://www.filecrate-example.net/s/qk72hdw01/Tildens_05.jpg

Pictures of About us

https://www.filecrate-example.net/sh/zm40vrt88/AboutUsPhotos

Article about Tilden's
https://www.filecrate-example.net/s/wp31nbx57/TildensBiscuitBarn1.PDF
https://www.filecrate-example.net/s/hy65lcu29/TildensBiscuitBarn2.PDF

Reason: I was slow to update with information.

Reason: I am just getting feedback to the designs posted. I wasn't sure of the limited feedback was limiting designers from submitting designs. That and running a business with 25 employees open 12 hours a day, being here 2 hours prior and 2-3 hours after makes for long days.

I've increased the first place prize and also added funds to the second and third place prizes for your effort.

I just need the files in PSD, not HTML 5 as originally requested. We can handle getting the coding part.

Ill have the contest finalized by Monday. Thanks for your patience.

Target Market(s)

Cross section of adults from 18-35 & 35-55.

Industry/Entity Type

Industrial

Font styles to use
Other font styles liked:
• ff tisa web pro or garamond premier pro

Requirements
Must have
• Must be clean, look nice and not look like an afterthought.
Nice to have
• Please see the last two documents for information about our restaurant, which was featured in our local newspaper.

```html
<!DOCTYPE html>
<html lang="en">
<head>
<meta charset="utf-8">
<title>Tilden's Biscuit Barn</title>
<link rel="stylesheet" href="https://fonts.googleapis.com/css2?family=Poiret+One&family=Open+Sans:wght@400&family=Cormorant+Garamond:ital,wght@0,500;1,500&display=swap">
<style>
  :root {
    --page: #5e4637;
    --page-dark: #4f3a2d;
    --sidebar: #7a5f48;
    --panel: #523c2f;
    --panel-line: #6b5242;
    --cream: #efe0c4;
    --gold: #f3d9a6;
    --text-light: #f1e7da;
    --muted: #d8c6b2;
    --chalk: #d9a2d4;
    --board: #1f1d1e;
    --wood: #6e4b2f;
    --footer: #b9a48f;
    --footer-ink: #4a3a2e;
    --frame: #3b3029;
  }
  * { box-sizing: border-box; margin: 0; padding: 0; }
  html, body { width: 888px; height: 1200px; overflow: hidden; }
  body {
    position: relative;
    background: linear-gradient(90deg, var(--page-dark), var(--page) 15%, var(--page) 85%, var(--page-dark));
    font-family: "Open Sans", sans-serif;
    color: var(--text-light);
  }
  .abs { position: absolute; }
  .deco { font-family: "Poiret One", sans-serif; text-transform: uppercase; color: var(--cream); letter-spacing: 0.5px; }

  .sidebar { left: 92px; top: 0; width: 163px; height: 1056px; background: var(--sidebar); }
  .logo { left: 132px; top: 48px; width: 80px; height: 80px; border-radius: 50%; background: #e9d6a4; border: 3px solid #8a6a3e;
    display: flex; align-items: center; justify-content: center; font-family: "Open Sans", sans-serif; color: #b3312d; font-size: 15px; }
  .rule { left: 128px; width: 93px; height: 1px; background: #3f2f24; }
  .nav { left: 92px; width: 163px; text-align: center; font-size: 13px; }

  .chalkboard { left: 94px; top: 452px; width: 192px; height: 302px; background: linear-gradient(135deg, #7d5737, var(--wood) 50%, #5a3c25); border-radius: 10px; }
  .board { left: 118px; top: 478px; width: 144px; height: 250px; background: var(--board); }
  .chalk { font-family: "Cormorant Garamond", serif; color: var(--chalk); }
  .board-title { left: 132px; top: 492px; font-size: 15px; color: #e9dfe6; }
  .board-line { left: 132px; top: 515px; width: 92px; border-top: 1px dashed #8e8a8c; }
  .board-menu { left: 130px; top: 525px; width: 118px; font-size: 13px; line-height: 16px; text-align: justify; }

  .side-head { left: 114px; font-size: 14px; }
  .social { left: 114px; font-size: 10px; color: var(--muted); display: flex; align-items: center; gap: 9px; }
  .social .dot { width: 16px; height: 16px; border-radius: 50%; background: #d9cdbf; }
  .payment { left: 117px; top: 929px; font-size: 10px; line-height: 14px; color: var(--text-light); }

  .headline { left: 300px; top: 32px; font-size: 23px; letter-spacing: 0; }
  .frame { left: 350px; top: 76px; width: 398px; height: 276px; background: var(--frame); border: 6px solid #5a4a3e; box-shadow: 0 4px 10px rgba(0,0,0,.5); }
  .photo { left: 374px; top: 100px; width: 354px; height: 226px; background: linear-gradient(160deg, #c9b38d, #8e6f52 60%, #5a4d52); }

  .panel { left: 346px; width: 424px; background: var(--panel); border: 1px solid var(--panel-line); }
  .panel-title { left: 395px; font-size: 15px; }
  .sub { left: 395px; top: 456px; font-size: 8.5px; color: var(--gold); }
  .body-copy { left: 396px; top: 475px; width: 354px; font-size: 8.5px; line-height: 11.6px; text-align: justify; }
  .arrows { left: 712px; }
  .thumb { top: 670px; width: 103px; height: 84px; }
  .news-photo { left: 395px; top: 878px; width: 118px; height: 103px; background: linear-gradient(135deg, #a77d5d, #e0c3a0 50%, #6a5a66); }
  .news-title { left: 525px; top: 876px; font-size: 11px; color: var(--gold); }
  .news-copy { left: 525px; top: 891px; width: 215px; font-size: 8.4px; line-height: 11.5px; }

  .footer { left: 0; top: 1056px; width: 888px; height: 144px; background: var(--footer); border-top: 3px solid #3d2f25; }
  .foot-head { font-size: 14px; color: var(--footer-ink); top: 1072px; }
  .hours { left: 118px; top: 1106px; font-size: 11px; color: #2e241c; }
  .clock { left: 118px; top: 1132px; width: 45px; height: 64px; background: linear-gradient(#3a2f2a, #1d1816); border-radius: 22px 22px 4px 4px; }
  .contact { left: 350px; font-size: 9px; color: var(--footer-ink); display: flex; align-items: center; gap: 8px; }
  .contact svg { width: 10px; height: 10px; fill: var(--footer-ink); }
  .phone-shelf { left: 586px; top: 1084px; width: 210px; height: 100px; background: linear-gradient(#a28569, #6f4d33); border-radius: 6px; }
</style>
</head>
<body>
  <div class="abs sidebar"></div>
  <div class="abs logo">Tilden's</div>
  <div class="abs rule" style="top:176px"></div>
  <nav>
    <div class="abs nav deco" style="top:200px">Home</div>
    <div class="abs nav deco" style="top:232px">About Us</div>
    <div class="abs nav deco" style="top:264px">Menu</div>
    <div class="abs nav deco" style="top:296px">Location</div>
  </nav>
  <div class="abs rule" style="top:360px"></div>

  <div class="abs chalkboard"></div>
  <div class="abs board"></div>
  <div class="abs chalk board-title">Today's Menu</div>
  <div class="abs board-line"></div>
  <div class="abs chalk board-menu">Senior menu $5.99 to $7.99 breakfast $4.59 to $10.99 burgers and sandwiches $6.99 to $10.99 cold cuts and salads $6.99 to $9.49, child's menu $3.29 to $4.69</div>

  <div class="abs deco side-head" style="top:787px">Follow Us</div>
  <div class="abs social" style="top:818px"><span class="dot"></span>Barnboard</div>
  <div class="abs social" style="top:840px"><span class="dot"></span>Chirpline</div>
  <div class="abs social" style="top:863px"><span class="dot"></span>Rss Blog</div>
  <div class="abs deco side-head" style="top:901px">Payment</div>
  <div class="abs payment">MeridianCard<br>Vantage<br>Atlas Express<br>Compass and<br>Personal checks accepted.</div>

  <h1 class="abs deco headline" style="font-weight:400">Get Happy at Tilden's Biscuit Barn Est 1999</h1>
  <div class="abs frame"></div>
  <div class="abs photo" role="img" aria-label="Busy diner interior with guests at tables and memorabilia on the walls"></div>

  <section>
    <div class="abs panel" style="top:382px;height:195px"></div>
    <h2 class="abs deco panel-title" style="top:424px;font-weight:400">Welcome to Tilden's</h2>
    <div class="abs sub">TILDEN'S: QUALITY OF FOOD APPEALS TO BOTH PARTIES</div>
    <p class="abs body-copy">They then transitioned into a story from junior high with all the details of the most hated boy in their class and his misadventures. Eventually the conversation came back to politics and personal strengths and weaknesses of each of the Republican presidential candidates. Mark them undecided at this stage of the race.</p>
  </section>

  <section>
    <div class="abs panel" style="top:597px;height:195px"></div>
    <h2 class="abs deco panel-title" style="top:636px;font-weight:400">Gallery</h2>
    <svg class="abs arrows" style="top:643px" width="22" height="12" viewBox="0 0 22 12"><path d="M9 0v12L0 6z M13 0v12l9-6z" fill="#e8e0d6"/></svg>
    <div class="abs thumb" style="left:393px;background:linear-gradient(135deg,#f4ede4,#c47a36 50%,#f0e6da)" role="img" aria-label="Plate of french toast"></div>
    <div class="abs thumb" style="left:512px;background:linear-gradient(135deg,#ffffff,#c99a68 50%,#ffffff)" role="img" aria-label="Sandwich with lettuce"></div>
    <div class="abs thumb" style="left:631px;background:linear-gradient(135deg,#3b4f8a,#d79a3c 50%,#8a3a1e)" role="img" aria-label="Cheeseburger with fries"></div>
  </section>

  <section>
    <div class="abs panel" style="top:813px;height:194px"></div>
    <h2 class="abs deco panel-title" style="top:845px;font-weight:400">News &amp; Events</h2>
    <svg class="abs arrows" style="top:860px" width="22" height="12" viewBox="0 0 22 12"><path d="M9 0v12L0 6z M13 0v12l9-6z" fill="#e8e0d6"/></svg>
    <div class="abs news-photo" role="img" aria-label="Server carrying plates of food through the diner"></div>
    <h3 class="abs news-title" style="font-weight:400">Dining Out</h3>
    <p class="abs news-copy">Forgotten day for the Golden State Please see ADMISSION / D2 Good food, and lots of it, keeps them coming back Pioneer Daughters of the Valley, Oak Creek Parlor No. 239<br>What: California Admission Day luncheon<br>When: 11:30 a.m. Friday<br>Where: Timber Trail Grill,<br>3580 Meadowlark Highway</p>
  </section>

  <footer>
    <div class="abs footer"></div>
    <h2 class="abs deco foot-head" style="left:118px;font-weight:400">Hours</h2>
    <div class="abs hours">5:30 a.m. to 2 p.m.Daily.</div>
    <div class="abs clock" role="img" aria-label="Antique mantel clock"></div>
    <h2 class="abs deco foot-head" style="left:346px;font-weight:400">Contact Us</h2>
    <div class="abs contact" style="top:1106px"><svg viewBox="0 0 10 10"><path d="M5 0L0 5h1.5v5h2.5V7h2v3h2.5V5H10z"/></svg>10595 MEADOWLARK HIGHWAY 555-0142</div>
    <div class="abs contact" style="top:1125px"><svg viewBox="0 0 10 10"><path d="M2 0l2 2.5-1.2 1.3c.7 1.4 1.9 2.6 3.4 3.4L7.5 6 10 8 8.5 10C4 9.5.5 6 0 1.5z"/></svg>+1-555-019-4420</div>
    <div class="abs contact" style="top:1144px"><svg viewBox="0 0 10 10"><path d="M0 2h10v1L5 6 0 3zM0 4l5 3 5-3v4H0z"/></svg>info@tildensbiscuitbarn.example</div>
    <div class="abs contact" style="top:1163px"><svg viewBox="0 0 10 10"><path d="M0 2h10v1L5 6 0 3zM0 4l5 3 5-3v4H0z"/></svg>tildensbiscuitbarn.example</div>
    <div class="abs phone-shelf" role="img" aria-label="Vintage telephone and open book on a wooden shelf"></div>
  </footer>
</body>
</html>
```